Business Card Design

- one on one personal training
- group personal training
- indoor or outdoor training available
- fitness and health assessments
- personalised fitness programs
- flexible hours for training

I am a Personal Trainer in Perth Australia. I am looking to expand my word of mouth client base.

I would like to see something that uses the colours blue, green and/or yellow.

The final design should reflect the way that I train clients, fun, motivating and perhaps a little quirky?
Updates

update with a logo with the letters MPT thank you

Hi all, Have had some great designs so far. Have decided to go double sided, perhaps to use the back to list my services. Thank you

Please check update brief. Thank you.

Target Market(s)

Professionals, ages 30 to 60

Industry/Entity Type

Training

Contact Information for Business Card

Mandy Whitlock
Personal Trainer

0471 208 514
mandypersonaltrainer@fitmailbox.example
http://www.mandypersonaltrainer.example

Requirements
Must have
• A logo with the letter MPT
Nice to have
• a logo to represent either; fitness, health, change, overall well-being.
Should not have
• Please no weights or lotus flowers!!

```html
<!DOCTYPE html>
<html lang="en">
<head>
<meta charset="utf-8">
<title>Mandy Whitlock – Personal Trainer Business Card</title>
<link rel="stylesheet" href="https://fonts.googleapis.com/css2?family=Arimo:wght@400;700&display=swap">
<style>
  :root {
    --page-bg: #e4e4e2;
    --card-dark: #1b1e22;
    --card-mid: #262a30;
    --band: #050505;
    --accent-red: #e0213a;
    --accent-blue: #1fa3e0;
    --text-light: #f2f2f2;
    --text-soft: #d6d6d6;
  }
  * { margin: 0; padding: 0; box-sizing: border-box; }
  html, body {
    width: 1200px;
    height: 873px;
    overflow: hidden;
    background: var(--page-bg);
    font-family: "Arimo", Arial, sans-serif;
  }
  .sheet {
    width: 1200px;
    height: 873px;
    display: flex;
    align-items: center;
    justify-content: center;
    gap: 40px;
  }
  .card {
    position: relative;
    width: 560px;
    height: 320px;
    border-radius: 4px;
    overflow: hidden;
    box-shadow: 0 6px 18px rgba(0,0,0,0.25);
  }
  .card-texture {
    position: absolute;
    inset: 0;
    background: radial-gradient(ellipse at 40% 35%, var(--card-mid) 0%, var(--card-dark) 70%);
  }
  .faint-ring {
    position: absolute;
    width: 190px;
    height: 190px;
    border-radius: 50%;
    border: 26px solid rgba(255,255,255,0.05);
  }
  .card-front .faint-ring { right: 40px; top: 110px; }
  .card-back .faint-ring { left: 30px; top: -60px; }
  .card-band {
    position: absolute;
    left: 0; bottom: 0;
    width: 100%;
    height: 90px;
  }
  .brand-mark {
    position: absolute;
    display: flex;
    align-items: center;
    gap: 10px;
    color: var(--text-light);
    font-weight: 700;
  }
  .brand-dot {
    border-radius: 50%;
    background: var(--accent-blue);
  }
  .card-front .brand-mark { left: 40px; top: 34px; font-size: 34px; }
  .card-front .brand-dot { width: 40px; height: 40px; }
  .card-back .brand-mark { right: 28px; bottom: 104px; font-size: 12px; gap: 5px; }
  .card-back .brand-dot { width: 12px; height: 12px; }
  .contact {
    position: absolute;
    left: 180px;
    top: 92px;
    color: var(--text-light);
    font-size: 17px;
    line-height: 1.35;
  }
  .contact-name { font-size: 19px; }
  .contact-role { color: var(--text-soft); margin-bottom: 4px; }
  .contact-line { display: flex; align-items: center; gap: 8px; }
  .contact-line svg { width: 15px; height: 15px; flex: none; }
  .services {
    position: absolute;
    left: 44px;
    top: 34px;
    color: var(--text-light);
    font-size: 18px;
    line-height: 1.3;
    list-style: none;
  }
  .services-title { font-size: 19px; margin-bottom: 2px; }
</style>
</head>
<body>
<main class="sheet">

  <section class="card card-front" aria-label="Business card front">
    <div class="card-texture" role="img" aria-label="Dark perforated leather texture"></div>
    <div class="faint-ring" aria-hidden="true"></div>
    <div class="brand-mark"><span class="brand-dot"></span>MPT</div>
    <div class="contact">
      <p class="contact-name">Mandy Whitlock</p>
      <p class="contact-role">Personal Trainer</p>
      <p class="contact-line">
        <svg viewBox="0 0 16 16" fill="none" stroke="currentColor" stroke-width="1.4"><path d="M4 1.5h3l1 3-2 1.3a8 8 0 0 0 4.2 4.2L11.5 8l3 1v3a2 2 0 0 1-2 2A11 11 0 0 1 2 3.5a2 2 0 0 1 2-2z"/></svg>
        0471 208 514
      </p>
      <p class="contact-line">
        <svg viewBox="0 0 16 16" fill="none" stroke="currentColor" stroke-width="1.4"><rect x="1.5" y="3.5" width="13" height="9"/><path d="M1.5 3.5 8 9l6.5-5.5"/></svg>
        mandypersonaltrainer@fitmailbox.example
      </p>
      <p class="contact-line">
        <svg viewBox="0 0 16 16" fill="none" stroke="currentColor" stroke-width="1.3"><circle cx="8" cy="8" r="6.5"/><ellipse cx="8" cy="8" rx="3" ry="6.5"/><path d="M1.5 8h13M2.5 4.8h11M2.5 11.2h11"/></svg>
        www.mandypersonaltrainer.example
      </p>
    </div>
    <svg class="card-band" viewBox="0 0 560 90" preserveAspectRatio="none" aria-hidden="true">
      <path d="M0 40 C 150 18, 380 14, 560 58 L560 90 L0 90 Z" fill="var(--band)"/>
      <path d="M0 40 C 150 18, 380 14, 560 58" fill="none" stroke="var(--accent-red)" stroke-width="2"/>
    </svg>
  </section>

  <section class="card card-back" aria-label="Business card back">
    <div class="card-texture" role="img" aria-label="Dark perforated leather texture"></div>
    <div class="faint-ring" aria-hidden="true"></div>
    <ul class="services">
      <li class="services-title">Offer</li>
      <li>- One on one personal training</li>
      <li>- Group personal training</li>
      <li>- Indoor or outdoor training available</li>
      <li>- Fitness and health assessments</li>
      <li>- Personalized fitness programs</li>
    </ul>
    <div class="brand-mark"><span class="brand-dot"></span>MPT</div>
    <svg class="card-band" viewBox="0 0 560 90" preserveAspectRatio="none" aria-hidden="true">
      <path d="M0 66 C 180 64, 380 62, 560 60 L560 90 L0 90 Z" fill="var(--band)"/>
      <path d="M0 66 C 180 64, 380 62, 560 60" fill="none" stroke="var(--accent-red)" stroke-width="2"/>
    </svg>
  </section>

</main>
</body>
</html>
```